New Wordpress Design Project

The website is my name tessamaybrook.com

I need a website design that will be graphically pleasing and have a crisp feel to it. I am a business and personal coach and have many different niches that I work with. I am looking for the central site to describe who I am and how I help people - I help people "wake up" to make conscious choices in their lives. I use hypnosis but do not want it to be esoteric, I ground the hypnosis and base it in science of how people can manage their state to reach their full potential in their lives and in business. I work one on one but also do public speaking and recently started to do trainings with corporations, helping people improve their business. I am looking at this as a merge of hypnosis and other tools with the business or corporate world - based in science - neuroplasticity, brain training etc. I will be helping people to overcome anxiety and stress, limiting beliefs, controlling and choosing habits that will work for them, fears and phobias, golf/sports improvement, weight loss.

Really helping people to center back with themselves, to not be so caught up in their head but drop into their heart and with what is really going on. My mission is to connect them back with themselves, using language, state and conscious choice.

I work online with entrepreneurs helping them to get unstuck, move past fears and limiting beliefs to create the business of their dreams.

I added a file of what I am envisioning on the right hand side of my site to show people the different niches I am involved with.

Some sites that I like www.gretavanholt.com www.corinnemaddox.org http://www.judekestrel.com/ , Details for my new Wordpress Design Project will be added soon. , The website is my name tessamaybrook.com

the square boxes graphic below is similar to one that I will be making for a page on my site for clarity and crispness. But will be creating it more in the teal color.

Target Market(s)

My target market are both male and female 30-50 either entreprenuers/business people

Industry/Entity Type

Training

Requirements
Must have
• A video with an opt in box
My background color is teal/blue (see below file)
Social media links

```html
<!DOCTYPE html>
<html lang="en">
<head>
<meta charset="utf-8">
<title>TessaMayBrook.com – Blog</title>
<link href="https://fonts.googleapis.com/css2?family=Lobster&family=Open+Sans:ital,wght@0,400;0,600;1,400&display=swap" rel="stylesheet">
<style>
:root{
  --outer:#4d4d4d;
  --page:#ffffff;
  --teal:#19a7b3;
  --body-text:#7a7a7a;
  --meta:#8a8a8a;
  --heading:#2b2b2b;
  --sidebar-bg:#f1f3f2;
  --sidebar-border:#d9dcdb;
  --footer-top:#3f3f3f;
  --footer-text:#bdbdbd;
  --footer-rule:#555;
}
*{margin:0;padding:0;box-sizing:border-box}
html,body{width:1200px;height:1000px;overflow:hidden;background:#fff}
body{font-family:"Open Sans",Arial,sans-serif;position:relative}
a{color:var(--teal);text-decoration:none}
.backdrop{position:absolute;left:0;top:0;width:1200px;height:734px;background:var(--outer)}
.page{position:absolute;left:43px;top:0;width:1114px;height:343px;background:var(--page)}
.abs{position:absolute}
.nowrap{white-space:nowrap}

/* post */
.post-title{left:197px;top:-20px;font-family:"Lobster",cursive;font-size:26px;color:var(--heading);white-space:nowrap}
.post-meta{left:197px;top:16px;width:506px;height:21px;border-bottom:1px dashed #cfcfcf;font-size:11.5px;font-style:italic;color:var(--meta);display:flex;align-items:flex-start;gap:4px;white-space:nowrap}
.post-meta svg{margin-right:2px;margin-top:1px}
.post-thumb{left:197px;top:58px;width:155px;height:155px;border:1px solid #cfcfcf;padding:6px;background:#fff}
.post-thumb div{width:100%;height:100%;background:radial-gradient(circle at 55% 45%,#d8c23a 0%,#a9a42a 40%,#4f5a20 75%,#2e3516 100%)}
.post-excerpt{left:367px;top:51px;font-size:11.5px;line-height:20.6px;color:var(--body-text);white-space:nowrap}
.post-terms{left:197px;top:227px;font-size:11.5px;line-height:14px;font-style:italic;color:var(--meta);white-space:nowrap}
.read-more{left:618px;top:231px;width:85px;height:25px;border:1px solid #c9c9c9;border-radius:3px;background:linear-gradient(#f4f4f4,#dcdcdc);font-size:12px;color:#7a7a7a;text-align:center;line-height:23px}

/* sidebar */
.sidebar-box{left:771px;top:-10px;width:233px;height:157px;background:var(--sidebar-bg);border:1px solid var(--sidebar-border);border-radius:5px}
.side-list{left:791px;top:10px;width:200px;list-style:none;font-size:11.5px;line-height:17px;color:var(--body-text);white-space:nowrap}
.side-list li{position:relative;padding-left:23px;margin-bottom:9px}
.side-list svg{position:absolute;left:0;top:2px}

/* footer */
.footer{position:absolute;left:43px;top:343px;width:1114px;height:347px;border-top:4px solid #c8c8c8;
  background:radial-gradient(ellipse 500px 180px at 50% 0,#5a5a5a 0%,var(--footer-top) 55%,#333 100%);box-shadow:0 3px 6px rgba(0,0,0,.35)}
.footer-col{position:absolute;top:392px;width:250px}
.footer-col h3{font-family:"Lobster",cursive;font-weight:400;font-size:21px;color:#fff;padding-bottom:5px;border-bottom:1px solid var(--footer-rule);margin-bottom:20px;white-space:nowrap}
.footer-col p{font-size:11.6px;line-height:22.5px;color:var(--footer-text);white-space:nowrap}
.footer-list{list-style:none;font-size:11.6px;color:var(--footer-text)}
.footer-list li{position:relative;padding-left:23px;height:27.5px;line-height:20px;white-space:nowrap}
.footer-list svg{position:absolute;left:0;top:3px}
.succeed-thumb{float:left;width:74px;height:54px;border:2px solid #e8e8e8;margin:5px 14px 5px 0;background:linear-gradient(135deg,#2fb7bd,#7fd3d0 55%,#e7f4f1)}
.bottom-bar{position:absolute;left:43px;top:631px;width:1114px;height:59px;border-top:1px solid #454545;background:linear-gradient(#343434,#262626);text-align:center;font-size:11px;line-height:59px;color:#888}
.bottom-bar a{color:#cfcfcf}
</style>
</head>
<body>
<div class="backdrop"></div>
<div class="page"></div>

<h2 class="abs post-title">Quisque non faucibus nisi.</h2>
<div class="abs post-meta">
  <svg width="14" height="12" viewBox="0 0 14 12"><rect x="1" y="2" width="9" height="9" fill="none" stroke="#888" stroke-width="1.4"/><path d="M5 7 L12 0 L14 2 L7 9 L5 9 Z" fill="#888"/></svg>
  <span>Written by <a href="#">TESSA MAY</a> on <a href="#">December 7, 2012</a> |</span>
  <svg width="14" height="12" viewBox="0 0 14 12" style="margin-left:4px"><ellipse cx="6" cy="5" rx="5.5" ry="4" fill="none" stroke="#888" stroke-width="1.3"/><path d="M3 8 L2 11 L6 9" fill="#888"/></svg>
  <a href="#">436 comments</a>
</div>
<div class="abs post-thumb"><div role="img" aria-label="Close-up photo of a yellow autumn leaf"></div></div>
<p class="abs post-excerpt">Sit voluptatem accusantium doloremque laudantium, totam<br>rem aperiam, eaque ipsa quae ab illo inventore veritatis et quasi<br>architecto beatae vitae dicta sunt explicabo. Nemo enim ipsam<br>voluptatem quia voluptas sit aspernatur aut odit aut fugit, sed<br>quia consequuntur magni dolores eos qui ratione voluptatem<br>sequi nesciunt. Neque porro quisquam est, qui dolorem ipsum<br>quia dolor sit amet, consectetur, adipisci velit, sed quia non<br>numquam eius modi tempora in.</p>
<div class="abs post-terms">Categories: <a href="#">Limiting Beliefs</a><br>Tags: <a href="#">beliefs</a>, <a href="#">change</a>, <a href="#">desire</a>, <a href="#">money</a>.</div>
<a class="abs read-more" href="#">Read More</a>

<div class="abs sidebar-box"></div>
<ul class="abs side-list">
  <li><svg width="12" height="12" viewBox="0 0 12 12"><path d="M1 11 L11 1 C12 4 9 8 4 9 Z" fill="#8a8a8a"/></svg><a href="#">Dolore magna aliqua!</a><br>Morbi sodales, risus non nibh<br>luctus nulla, rutrum..</li>
  <li><svg width="12" height="12" viewBox="0 0 12 12"><path d="M1 11 L11 1 C12 4 9 8 4 9 Z" fill="#8a8a8a"/></svg><a href="#">Veniam, quis nostrudmetus...</a><br>Maecenas et felis metus. Donec<br>libero tincidunt in.</li>
</ul>

<div class="footer"></div>
<section class="footer-col" style="left:197px">
  <h3>Coaching Sessions</h3>
  <p>I offer one on one coaching as well as group<br>coaching. If you want to accelerate your success<br>then coaching sessions are the best way to<br>accomplish that. I really enjoy working with my<br>clients and seeing them become and achieve<br>what they want in life. Find out more here...</p>
</section>
<section class="footer-col" style="left:471px;width:246px">
  <h3>Launch Your Passion</h3>
  <ul class="footer-list">
    <li><svg width="12" height="12" viewBox="0 0 12 12"><path d="M1 11 L11 1 C12 4 9 8 4 9 Z" fill="#cfcfcf"/></svg>Dolore magna aliqua. Ut enim ad minim</li>
    <li><svg width="12" height="12" viewBox="0 0 12 12"><path d="M1 11 L11 1 C12 4 9 8 4 9 Z" fill="#cfcfcf"/></svg>Veniam, quis nostrud</li>
    <li><svg width="12" height="12" viewBox="0 0 12 12"><path d="M1 11 L11 1 C12 4 9 8 4 9 Z" fill="#cfcfcf"/></svg>Exercitation ullamco laboris nisi ut aliquip</li>
    <li><svg width="12" height="12" viewBox="0 0 12 12"><path d="M1 11 L11 1 C12 4 9 8 4 9 Z" fill="#cfcfcf"/></svg>Ea commodo consequat. Duis irure...</li>
    <li><svg width="12" height="12" viewBox="0 0 12 12"><path d="M1 11 L11 1 C12 4 9 8 4 9 Z" fill="#cfcfcf"/></svg>In reprehenderit in &nbsp;fugiat nulla pariatur...</li>
  </ul>
</section>
<section class="footer-col" style="left:746px;width:256px">
  <h3 style="width:248px">Help You Succeed!</h3>
  <div class="succeed-thumb" role="img" aria-label="Illustration of bare feet on a teal background"></div>
  <p>Lorem ipsum dolor sit amet,<br>consectetur adipisicing elit, sed<br>do eiusmod tempor incididunt<br>ut labore et dolore magna aliqua. Ut enim ad<br>minim veniam, quis nostrud exercitation ullamco<br>laboris nisi irure dolor in reprehenderit ...</p>
</section>

<div class="bottom-bar">Copyright © 2014 <a href="#">TessaMayBrook.com</a></div>
</body>
</html>
```